Business Cards & Stationery
Hollowmere Capital Group (Investment Firm)
Project: Business Cards & Stationery
Business Cards & Stationery  -
Creative Brief
Professional
Peter L. Vanstrom III
Registered Principal, OSJ
917 Larkspur Road Milbrook, WV 25418
peter.vanstrom@quillmark-example.com
www.HollowmereCapitalGroup-example.com
Also has to say (in smaller font): Securities and advisory services offered through Crestfield Ledger Corporation (CLC). Member TVORA/BQLX and a Registered Investment Advisor. Hollowmere Capital Group and CLC are separate and unrelated companies.
logo for Hollowmere Capital Group

```html
<!DOCTYPE html>
<html lang="en">
<head>
<meta charset="utf-8">
<title>Hollowmere Capital Group – Business Card</title>
<link href="https://fonts.googleapis.com/css2?family=Cinzel:wght@500&family=Tinos:wght@400;700&display=swap" rel="stylesheet">
<style>
  :root {
    --navy: #2c4a7e;
    --navy-deep: #233d6b;
    --silver: #b9bfc8;
    --ink: #1f2a3a;
    --paper: #ffffff;
    --page: #ffffff;
    --fine: #d3dbe8;
  }
  * { box-sizing: border-box; margin: 0; padding: 0; }
  html, body { width: 1200px; height: 336px; overflow: hidden; background: var(--page); }
  .sheet { position: relative; width: 1200px; height: 336px; }

  .card {
    position: absolute; top: 5px; width: 575px; height: 326px;
    box-shadow: 0 0 3px rgba(0,0,0,.25);
    overflow: hidden;
  }
  .card--front { left: 5px; background: var(--paper); }
  .card--back { left: 620px; background: var(--navy); }

  .card__wave { position: absolute; inset: 0; }

  .brand { position: absolute; display: flex; align-items: center; gap: 12px; }
  .brand__mark { width: 38px; height: 38px; flex: none; }
  .brand__name {
    font-family: "Cinzel", serif; font-weight: 500; letter-spacing: .04em;
    line-height: 1.15;
  }
  .card--front .brand { left: 18px; top: 16px; }
  .card--front .brand__mark { background: var(--navy); }
  .card--front .brand__name { color: var(--navy); font-size: 19px; }

  .card--back .brand { left: 50%; top: 50%; transform: translate(-50%, -50%); gap: 14px; }
  .card--back .brand__mark { width: 46px; height: 46px; border: 2px solid var(--paper); }
  .card--back .brand__name { color: var(--paper); font-size: 24px; }

  .person {
    position: absolute; right: 16px; top: 84px; text-align: right;
    font-family: "Tinos", serif;
  }
  .person__name { color: var(--navy); font-weight: 700; font-size: 17px; }
  .person__title { color: var(--ink); font-size: 12px; margin-top: 2px; }

  .contact {
    position: absolute; right: 16px; top: 222px; text-align: right;
    font-family: "Tinos", serif; font-style: normal;
    font-size: 12px; line-height: 15.5px; color: var(--paper);
  }
  .contact b { font-weight: 700; }

  .disclaimer {
    position: absolute; left: 16px; bottom: 12px; width: 230px;
    font-family: "Tinos", serif; font-size: 8px; line-height: 10px;
    color: var(--fine);
  }
</style>
</head>
<body>
<main class="sheet">
  <section class="card card--front">
    <svg class="card__wave" width="575" height="326" viewBox="0 0 575 326" aria-hidden="true">
      <defs>
        <linearGradient id="swoosh" x1="0" x2="1" y1="0" y2="0">
          <stop offset="0" stop-color="#e6e8ec"/>
          <stop offset=".5" stop-color="#9aa2ad"/>
          <stop offset="1" stop-color="#dfe2e7"/>
        </linearGradient>
      </defs>
      <path d="M0,236 C150,196 360,214 575,176 L575,192 C360,228 160,214 0,252 Z" fill="url(#swoosh)"/>
      <path d="M0,252 C160,214 360,228 575,192 L575,326 L0,326 Z" fill="var(--navy)"/>
    </svg>

    <div class="brand">
      <span class="brand__mark"></span>
      <span class="brand__name">Hollowmere<br>Capital Group</span>
    </div>

    <div class="person">
      <p class="person__name">Peter L. Vanstrom III</p>
      <p class="person__title">Registered Principal, OSJ</p>
    </div>

    <address class="contact">
      917 Larkspur Road<br>
      Milbrook, WV 25418<br>
      <b>Phone :</b> 304.555.0142<br>
      <b>Fax :</b> 304.555.0187<br>
      <b>Email :</b> peter.vanstrom@quillmark-example.com<br>
      <b>Web:</b> www.HollowmereCapitalGroup-example.com
    </address>

    <p class="disclaimer">Securities and advisory services offered through Crestfield Ledger Corporation (CLC). Member TVORA/BQLX and a Registered Investment Advisor. Hollowmere Capital Group and CLC are separate and unrelated companies.</p>
  </section>

  <section class="card card--back">
    <div class="brand">
      <span class="brand__mark"></span>
      <span class="brand__name">Hollowmere<br>Capital Group</span>
    </div>
  </section>
</main>
</body>
</html>
```